Direct Mail Postcard- Lighting Company

Our task is to send a postcard directly to houses surrounding where our company has done work. My goal is to position ourselves as the go to outdoor lighting partner for their neighborhood.
Trusted Lighting Design & Maintenance Your neighbor chose us to enhance and maintain their home's beauty and security. Now, we're offering our top-tier services to the entire neighborhood.
Please emphasize our:
Maintenance Excellence:
Regular system check-ups
Prompt repair and replacement
Upgrades to the latest technology
Less emphasis on:
Our Services:
High-Quality Landscape & Architectural Lighting
Reliable Permanent Lighting Solutions
Call us today and take advantage of our 25% discount (limited time offer)
For more details or to schedule a consultation, visit glowcrest-mo.com or call .
*Need to be able to tweak this for future campaigns. Quickly edit verbiage for future marketing campaigns. I.e. a file that can be edited through Canva
*Inspiration photo file (Yard Beacon Concepts)
*Would like to incorporate the before and after png
Call: (816) 555-0193
glowcrest-mo.com
Updates
I attached a new before and after photo. Please create a design implementing this
Look and feel
Each slider illustrates characteristics of the customer's brand and the style your logo design should communicate.

```html
<!DOCTYPE html>
<html lang="en">
<head>
<meta charset="UTF-8">
<title>Halvern Lighting – Neighborhood Postcard</title>
<link href="https://fonts.googleapis.com/css2?family=Poppins:wght@300;400;500;600;700;800;900&family=Great+Vibes&display=swap" rel="stylesheet">
<style>
  :root{
    --bg:#cfcfcf;
    --ink:#0a0a0a;
    --white:#ffffff;
    --gold:#c9a85a;
    --gold-light:#e2c77f;
    --gold-deep:#a88a43;
    --stamp:#e3e3e3;
    --rule:#9a9a9a;
  }
  *{box-sizing:border-box;margin:0;padding:0}
  html,body{width:804px;height:1200px;overflow:hidden}
  body{background:var(--bg);font-family:"Poppins",sans-serif;position:relative;color:var(--white)}
  .card{position:absolute;left:103px;width:599px;height:428px;overflow:hidden}
  .card--front{top:147px;background:var(--ink)}
  .card--back{top:626px;background:var(--white)}
  .abs{position:absolute}

  .brand-name{font-family:"Poppins",sans-serif;font-weight:500;color:var(--gold);font-size:20px;line-height:1;white-space:nowrap}

  /* front */
  .hero-photo{left:177px;top:0;width:422px;height:250px;
    background:radial-gradient(ellipse at 55% 55%,#b8682e 0%,#5a3a1a 25%,#24321a 55%,#0d130c 80%);}
  .hero-fade{left:177px;top:0;width:200px;height:250px;background:linear-gradient(90deg,var(--ink),rgba(10,10,10,0))}
  .hero-fade-bottom{left:177px;top:180px;width:422px;height:80px;background:linear-gradient(180deg,rgba(10,10,10,0),var(--ink))}
  .headline{left:26px;top:80px;font-weight:800;font-size:17px;line-height:21px}
  .headline__with{left:26px;top:119px;font-family:"Great Vibes",cursive;color:var(--gold);font-size:28px;line-height:1}
  .headline__premium{left:24px;top:136px;font-weight:800;font-size:44px;line-height:1;letter-spacing:-.8px}
  .headline__lighting{left:24px;top:173px;font-weight:800;font-size:44px;line-height:1;color:var(--gold);letter-spacing:-.8px}
  .intro{left:37px;top:223px;font-size:9.6px;line-height:11.5px;font-weight:500}
  .intro strong{color:var(--gold);font-weight:700}
  .offer-pill{left:27px;top:282px;width:300px;height:37px;border-radius:18px;
    background:linear-gradient(90deg,var(--gold-deep),var(--gold-light) 60%,var(--gold));padding:6px 0 0 12px;font-size:9.6px;line-height:11.5px}
  .offer-pill strong{font-weight:700}
  .polaroid{background:var(--white);padding:4px;box-shadow:0 2px 6px rgba(0,0,0,.5)}
  .polaroid div{width:100%;height:100%}

  .cta{font-weight:500;line-height:1.15}
  .cta__lead{font-size:10.5px;font-weight:600}
  .cta__sub{font-size:8px;color:var(--gold);letter-spacing:.2px}
  .cta__tag{display:inline-block;margin-top:4px;background:var(--gold);border-radius:7px;padding:1px 6px;font-size:6.8px;font-weight:700}
  .cta__rules{margin-top:5px;width:127px;height:18px;background:repeating-linear-gradient(180deg,var(--gold) 0 1px,transparent 1px 3px)}
  .discount{line-height:1}
  .discount__num{font-weight:900;font-size:52px;letter-spacing:-1px}
  .discount__num span{color:var(--gold);font-size:24px}
  .discount__word{font-weight:800;color:var(--gold);font-size:12.5px;letter-spacing:4.5px;margin-top:-4px}
  .discount__limit{font-size:8.6px;letter-spacing:2.6px;margin-top:2px}
  .divider{left:303px;top:370px;width:1px;height:33px;background:#777}
  .speak{left:326px;top:367px;font-size:9.2px;line-height:11px}
  .speak strong{color:var(--gold);font-weight:700;display:block}
  .phone-row{display:flex;align-items:center;gap:5px;font-weight:700}
  .web{font-weight:700;letter-spacing:.4px}

  /* back */
  .back-left{left:0;top:0;width:336px;height:428px;background:var(--ink);overflow:hidden}
  .back-photo{left:130px;top:210px;width:206px;height:218px;
    background:radial-gradient(ellipse at 60% 45%,#d7b47a 0%,#7a5c3a 25%,#2c3047 55%,#0f1420 80%)}
  .back-photo-fade{left:130px;top:210px;width:120px;height:218px;background:linear-gradient(90deg,var(--ink),rgba(10,10,10,0))}
  .services-title{left:26px;top:20px;font-weight:800;font-size:17px}
  .services-title span{color:var(--gold)}
  .service{display:flex;gap:5px;font-size:9.6px;line-height:11.5px}
  .icon-badge{flex:none;width:24px;height:24px;border-radius:50%;background:var(--gold);display:flex;align-items:center;justify-content:center}
  .maint-title{left:26px;top:92px;font-weight:700;color:var(--gold);font-size:10.6px}
  .maint-band{left:0;top:129px;width:336px;height:61px;display:flex}
  .maint-band__cell{flex:1;background:linear-gradient(180deg,var(--gold-light),var(--gold));border-right:1px solid var(--gold-deep);text-align:center;padding-top:23px;font-weight:700;font-size:9.6px;line-height:11.5px}
  .maint-icon{width:30px;height:30px;border-radius:50%;background:var(--white);border:1.5px solid var(--gold);display:flex;align-items:center;justify-content:center}
  .stamp{left:512px;top:27px;width:60px;height:65px;border-radius:4px;background:var(--stamp)}
  .address-line{left:361px;width:212px;height:1px;background:var(--rule)}
</style>
</head>
<body>

<!-- FRONT -->
<section class="card card--front">
  <div class="abs hero-photo" role="img" aria-label="Brick home at dusk with warm uplighting on the facade and trees"></div>
  <div class="abs hero-fade"></div>
  <div class="abs hero-fade-bottom"></div>

  <div class="abs brand-name" style="left:26px;top:32px">Halvern Lighting</div>

  <div class="abs headline">Elevate Your<br>Outdoor Spaces</div>
  <div class="abs headline__with">with</div>
  <div class="abs headline__premium">PREMIUM</div>
  <div class="abs headline__lighting">LIGHTING</div>

  <p class="abs intro">Trusted Lighting Design &amp; Maintenance<br>Your neighbor chose us to enhance and<br>maintain their <strong>home's beauty</strong><br><strong>and security</strong></p>

  <div class="abs offer-pill">Now, we're offering<br><strong>our top-tier services to the entire neighborhood</strong></div>

  <div class="abs polaroid" style="left:284px;top:237px;width:92px;height:98px;transform:rotate(-12deg)">
    <div role="img" aria-label="Modern home with colorful permanent roofline lighting" style="background:linear-gradient(160deg,#3b3f8f,#7a6cc0 45%,#2e3a2a)"></div>
  </div>
  <div class="abs polaroid" style="left:381px;top:240px;width:94px;height:94px">
    <div role="img" aria-label="Lit home and trees at night" style="background:radial-gradient(circle at 55% 45%,#b07a3a,#2a2d1a 65%)"></div>
  </div>
  <div class="abs polaroid" style="left:481px;top:238px;width:92px;height:98px;transform:rotate(12deg)">
    <div role="img" aria-label="Brick home with pathway lights at dusk" style="background:linear-gradient(170deg,#4a6a80,#8a4a2a 50%,#2b3a22)"></div>
  </div>

  <div class="abs cta" style="left:26px;top:341px">
    <div class="cta__lead">REACH OUT TODAY TO</div>
    <div class="cta__sub">SCHEDULE YOUR APPOINTMENT</div>
    <div class="cta__tag">AND TAKE ADVANTAGE OF OUR</div>
    <div class="cta__rules"></div>
  </div>

  <div class="abs discount" style="left:161px;top:335px">
    <div class="discount__num">25<span>%</span></div>
    <div class="discount__word">DISCOUNT</div>
    <div class="discount__limit">LIMITED TIME OFFER</div>
  </div>

  <div class="abs divider"></div>
  <div class="abs speak">SPEAK WITH<strong>A LIGHTING<br>DESIGNER</strong></div>

  <div class="abs" style="left:396px;top:365px">
    <div class="phone-row" style="font-size:19px">
      <svg width="19" height="19" viewBox="0 0 20 20"><circle cx="10" cy="10" r="9" fill="none" stroke="var(--gold)" stroke-width="2"/><path d="M6.5 5.5l2 0 1 2.5-1.3 1a6 6 0 0 0 2.8 2.8l1-1.3 2.5 1v2a1.2 1.2 0 0 1-1.3 1.2A8 8 0 0 1 5.3 6.8 1.2 1.2 0 0 1 6.5 5.5z" fill="var(--gold)"/></svg>
      (816) 555-0193
    </div>
    <div class="web" style="font-size:13.5px;margin-top:2px;margin-left:3px">www.glowcrest-mo.com</div>
  </div>
</section>

<!-- BACK -->
<section class="card card--back">
  <div class="abs back-left">
    <div class="abs back-photo" role="img" aria-label="Home entrance with lit columns and portico at dusk"></div>
    <div class="abs back-photo-fade"></div>

    <div class="abs services-title">Our <span>Services</span></div>
    <div class="abs service" style="left:26px;top:48px">
      <div class="icon-badge"><svg width="12" height="12" viewBox="0 0 12 12"><circle cx="6" cy="6" r="4.5" fill="none" stroke="#fff" stroke-width="1.2"/><path d="M4 6l1.5 1.5L8.3 4.6" fill="none" stroke="#fff" stroke-width="1.2"/></svg></div>
      <div>High-Quality<br>Landscape &amp;<br>Architectural Lighting</div>
    </div>
    <div class="abs service" style="left:184px;top:48px">
      <div class="icon-badge"><svg width="12" height="12" viewBox="0 0 12 12"><path d="M6 1a3.5 3.5 0 0 0-2 6.4V9h4V7.4A3.5 3.5 0 0 0 6 1zM4.5 10.5h3" fill="none" stroke="#fff" stroke-width="1.1"/></svg></div>
      <div>Reliable<br>Permanent Lighting<br>Solutions</div>
    </div>

    <div class="abs maint-title">Maintenance Excellence</div>
    <div class="abs maint-band">
      <div class="maint-band__cell">Regular<br>system<br>check-ups</div>
      <div class="maint-band__cell">Prompt<br>repair and<br>replacement</div>
      <div class="maint-band__cell" style="border-right:0">Upgrades to<br>the latest<br>technology</div>
    </div>
    <div class="abs maint-icon" style="left:41px;top:114px"><svg width="16" height="16" viewBox="0 0 16 16"><path d="M8 2a4.5 4.5 0 0 0-2.6 8.2V12h5.2v-1.8A4.5 4.5 0 0 0 8 2zM6 14h4M5.8 7.3l1.6 1.6 3-3" fill="none" stroke="#333" stroke-width="1"/></svg></div>
    <div class="abs maint-icon" style="left:153px;top:114px"><svg width="16" height="16" viewBox="0 0 16 16"><circle cx="8" cy="8" r="2.5" fill="none" stroke="#333"/><circle cx="8" cy="8" r="5.5" fill="none" stroke="#333" stroke-dasharray="2 1.4"/></svg></div>
    <div class="abs maint-icon" style="left:262px;top:114px"><svg width="16" height="16" viewBox="0 0 16 16"><path d="M8 2a4.5 4.5 0 0 0-2.6 8.2V12h5.2v-1.8A4.5 4.5 0 0 0 8 2zM6 14h4M8 5v4M6.5 6.5L8 5l1.5 1.5" fill="none" stroke="#333" stroke-width="1"/></svg></div>

    <div class="abs cta" style="left:27px;top:204px">
      <div class="cta__lead">REACH OUT TODAY TO</div>
      <div class="cta__sub">SCHEDULE YOUR APPOINTMENT</div>
      <div class="cta__tag">AND TAKE ADVANTAGE OF OUR</div>
    </div>
    <div class="abs discount" style="left:162px;top:203px">
      <div class="discount__num" style="font-size:27px">25<span style="font-size:13px">%</span></div>
      <div class="discount__word" style="font-size:7.2px;letter-spacing:2.5px;margin-top:-2px">DISCOUNT</div>
      <div class="discount__limit" style="font-size:5px;letter-spacing:1.5px">LIMITED TIME OFFER</div>
    </div>

    <div class="abs polaroid" style="left:29px;top:264px;width:64px;height:62px;transform:rotate(-5deg);padding:3px 3px 9px">
      <div role="img" aria-label="Home at night before lighting" style="background:linear-gradient(160deg,#2a2a22,#0f120d)"></div>
      <span style="position:absolute;left:7px;bottom:0;font-size:5px;color:#555">Before</span>
    </div>
    <div class="abs polaroid" style="left:96px;top:260px;width:62px;height:62px;transform:rotate(4deg);padding:3px 3px 9px">
      <div role="img" aria-label="Home at night after lighting" style="background:radial-gradient(circle at 55% 45%,#cfc3a0,#3a3a2a 60%,#11140f)"></div>
      <span style="position:absolute;left:6px;bottom:0;font-size:5px;color:#555">After</span>
    </div>

    <div class="abs" style="left:26px;top:343px;font-size:9.6px;line-height:11px">SCHEDULE A CONSULTATION<br><strong style="color:var(--gold);font-weight:700">OR SPEAK WITH A LIGHTING DESIGNER</strong></div>
    <div class="abs" style="left:26px;top:368px">
      <div class="phone-row" style="font-size:16.5px">
        <svg width="16" height="16" viewBox="0 0 20 20"><circle cx="10" cy="10" r="9" fill="none" stroke="var(--gold)" stroke-width="2"/><path d="M6.5 5.5l2 0 1 2.5-1.3 1a6 6 0 0 0 2.8 2.8l1-1.3 2.5 1v2a1.2 1.2 0 0 1-1.3 1.2A8 8 0 0 1 5.3 6.8 1.2 1.2 0 0 1 6.5 5.5z" fill="var(--gold)"/></svg>
        (816) 555-0193
      </div>
      <div class="web" style="font-size:11px;margin-left:1px">www.glowcrest-mo.com</div>
    </div>
  </div>

  <div class="abs brand-name" style="left:359px;top:34px;font-size:18px">Halvern Lighting</div>
  <div class="abs stamp"></div>
  <div class="abs address-line" style="top:244px"></div>
  <div class="abs address-line" style="top:277px"></div>
  <div class="abs address-line" style="top:310px"></div>
</section>

</body>
</html>
```